Lantern Quillhouse Website

Create website for Legal Management Company which specializes in Law Office Spersriinal Management
System implementation & Training
Global presence
Paralegal Services - Remote or In-Office
Legal Research
- Judge Motion Ruling History
- Opposing Counsel Opposition Research - Historical Filings - Pattern identification
Service by Mail - Ex- Parte Notice

Probate -Heir Finder - Asset Location -

```html
<!DOCTYPE html>
<html lang="en">
<head>
<meta charset="utf-8">
<title>Lantern Quillhouse — Legal Management</title>
<link href="https://fonts.googleapis.com/css2?family=Montserrat:ital,wght@0,400;0,500;0,600;0,700;1,400&display=swap" rel="stylesheet">
<style>
:root{
  --black:#000000;
  --ink:#111111;
  --text:#333333;
  --gold:#e8ad08;
  --gold-dark:#c99406;
  --cream:#fdf0cc;
  --card:#fdf1cf;
  --dark:#2a2e32;
  --dark-teal:#23302f;
  --mist:#e9eaec;
  --white:#ffffff;
}
*{box-sizing:border-box;margin:0;padding:0}
html,body{width:1200px;height:3761px;overflow:hidden}
body{font-family:'Montserrat',sans-serif;color:var(--text);background:var(--white);position:relative}
.abs{position:absolute}
a{color:inherit;text-decoration:none}

/* nav */
.topbar{left:0;top:0;width:1200px;height:80px;background:var(--black)}
.brand{left:137px;top:30px;font-weight:700;font-size:18px;color:var(--white);letter-spacing:.3px}
.brand span{color:var(--gold)}
.nav{left:447px;top:29px;display:flex;gap:30px;font-size:13px;color:var(--white);font-weight:500}
.nav .active{position:relative}
.nav .active::after{content:"";position:absolute;left:-4px;right:-4px;top:46px;height:2px;background:var(--gold)}

/* hero */
.hero{left:0;top:80px;width:1200px;height:621px;background:linear-gradient(100deg,#f4f1ec 0%,#e9e4dc 35%,#c9c3bb 60%,#d7d5d2 100%)}
.hero-title{left:130px;top:220px;font-size:40px;font-weight:700;color:var(--ink);line-height:1.18}
.hero-text{left:132px;top:380px;width:440px;font-size:13.5px;line-height:1.3;color:var(--ink)}
.btn{display:flex;align-items:center;justify-content:space-between;background:var(--gold);color:var(--ink);font-weight:600;border-radius:22px;padding:0 5px 0 20px;height:40px;font-size:16px}
.btn .arrow{width:32px;height:32px;border-radius:50%;background:var(--white);display:flex;align-items:center;justify-content:center}
.hero-btn{left:130px;top:461px;width:172px}
.dots{left:540px;top:595px;display:flex;gap:10px}
.dots i{display:block;width:22px;height:3px;background:var(--white)}
.dots i:first-child{background:var(--gold)}

/* about */
.about-photo{left:601px;top:696px;width:599px;height:552px;border-top-left-radius:80px;background:linear-gradient(135deg,#d9dfe6,#b9c6d4 45%,#8fa3b8 100%)}
.h2{font-weight:700;color:var(--ink)}
.about-title{left:158px;top:810px;font-size:33px}
.about-text{left:154px;top:866px;width:420px;font-size:14.5px;line-height:1.65}
.about-text p+p{margin-top:22px}
.about-btn{left:152px;top:1058px;width:163px}
.mission{left:137px;top:1117px;width:542px;height:185px;background:var(--cream);border-radius:14px;padding:28px 36px}
.mission h3{font-size:28px;font-weight:700;color:var(--ink);margin-bottom:18px}
.mission p{font-size:14.5px;line-height:1.65}
.badge{left:541px;top:1047px}

/* services */
.services{left:0;top:1365px;width:1200px;height:609px;background:linear-gradient(180deg,#30353a,#22272b 70%,#3a3f44)}
.services-title{left:0;top:1412px;width:1200px;text-align:center;font-size:33px;font-weight:700;color:var(--white)}
.svc-arrows{left:1049px;top:1427px;display:flex;gap:6px}
.svc-arrows span{width:30px;height:30px;border-radius:50%;background:var(--gold);display:flex;align-items:center;justify-content:center}
.card{top:1489px;width:247px;height:342px;background:var(--card);border-radius:8px;padding:18px 16px}
.card .ph{width:100%;height:194px;border-radius:2px}
.card h4{margin-top:22px;font-size:16px;font-weight:700;color:var(--ink);line-height:1.5;text-transform:uppercase}
.card p{margin-top:8px;font-size:14px;line-height:1.3;color:var(--ink)}
.card.featured{background:#6b5a2a;height:397px}
.card.featured h4,.card.featured p{color:var(--white)}

/* global */
.global{left:0;top:1974px;width:1200px;height:311px;background:linear-gradient(90deg,#d7d9dc,#eeeff1 45%,#e4e5e7)}
.global-title{left:0;top:2032px;width:1200px;text-align:center;font-size:33px}
.global-text{left:230px;top:2090px;width:740px;text-align:center;font-size:14.5px;line-height:1.65}

/* why */
.why-photo{left:577px;top:2237px;width:623px;height:487px;border-top-left-radius:60px;background:linear-gradient(135deg,#cfd6dd,#9aa8b4 50%,#4a4f4f 100%)}
.why-panel{left:0;top:2285px;width:679px;height:470px;background:var(--white);border-top-right-radius:50px}
.why-title{left:149px;top:2336px;font-size:33px}
.why-list{left:150px;top:2414px;width:440px;list-style:none;font-size:14.5px;line-height:1.4}
.why-list li{position:relative;padding-left:30px;margin-bottom:15px}
.why-list li::before{content:"";position:absolute;left:0;top:9px;width:14px;height:2px;background:var(--gold)}
.why-btn{left:149px;top:2619px;width:165px}

/* cta */
.cta{left:0;top:2774px;width:1200px;height:452px;background:linear-gradient(180deg,#1f2a2b,#2c3b3c 60%,#1e2829)}
.cta-title{left:0;top:2870px;width:1200px;text-align:center;font-size:42px;font-weight:700;color:var(--white)}
.cta-text{left:230px;top:2930px;width:740px;text-align:center;font-size:15.5px;line-height:1.22;color:var(--white)}
.cta-strong{left:280px;top:3003px;width:640px;text-align:center;font-size:15.5px;font-weight:700;line-height:1.25;color:var(--white)}
.cta-btn{left:521px;top:3066px;width:159px}

/* subscribe */
.subscribe{left:136px;top:3166px;width:928px;height:282px;background:var(--white);border-radius:24px;box-shadow:0 4px 18px rgba(0,0,0,.08)}
.sub-title{left:0;top:3218px;width:1200px;text-align:center;font-size:33px}
.sub-label{left:0;top:3270px;width:1200px;text-align:center;font-size:15px;color:var(--ink)}
.field{left:253px;top:3302px;width:693px;height:50px;border-radius:25px;background:#efefef;display:flex;align-items:center;justify-content:space-between;padding:0 4px 0 20px;font-size:15px;color:var(--ink)}
.field .submit{background:var(--gold);border-radius:21px;height:42px;width:114px;display:flex;align-items:center;justify-content:center;font-weight:700;font-size:16px}
.sub-note{left:270px;top:3364px;font-size:15px;font-style:italic;color:var(--gold)}

/* footer */
.foot-brand{left:0;top:3527px;width:1200px;text-align:center;font-size:18px;font-weight:700;color:var(--ink)}
.foot-nav{left:0;top:3582px;width:1200px;display:flex;justify-content:center;gap:28px;font-size:13px;color:var(--ink)}
.social{left:531px;top:3629px;display:flex;gap:12px}
.social span{width:38px;height:38px;border-radius:50%;background:var(--black)}
.social span:first-child{background:var(--gold)}
.bottombar{left:0;top:3710px;width:1200px;height:51px;background:var(--black);color:var(--white);font-size:14px}
.bottombar .l{position:absolute;left:140px;top:18px}
.bottombar .r{position:absolute;right:135px;top:18px}
</style>
</head>
<body>

<header>
  <div class="abs topbar"></div>
  <div class="abs brand">LANTERN <span>QUILLHOUSE</span></div>
  <nav class="abs nav">
    <a class="active">HOME</a><a>ABOUT US</a><a>SERVICES</a><a>WHY CHOOSE US</a><a>TESTIMONIALS</a><a>CONTACT US</a>
  </nav>
</header>

<section>
  <div class="abs hero" role="img" aria-label="Photo of a professional woman reviewing documents at a laptop in a bright office"></div>
  <h1 class="abs hero-title">Strategic Legal<br>Management.<br>Intelligent Support.</h1>
  <p class="abs hero-text">Lorem ipsum dolor sit amet, consectetur adipiscing elit, sed do eiusmod tempor incididunt ut labore et dolore magna aliqua. Quis ipsum suspendisse ultrices gravida.</p>
  <a class="abs btn hero-btn">Get Started <span class="arrow"><svg width="18" height="14" viewBox="0 0 18 14"><path d="M1 7h15M10 1l6 6-6 6" fill="none" stroke="#111" stroke-width="2"/></svg></span></a>
  <div class="abs dots"><i></i><i></i><i></i><i></i></div>
</section>

<section>
  <div class="abs about-photo" role="img" aria-label="Photo of two colleagues discussing paperwork at a desk"></div>
  <h2 class="abs h2 about-title">About Us</h2>
  <div class="abs about-text">
    <p>We partner with law firms, solo practitioners, and legal departments to improve efficiency, compliance, and strategic decision-making.</p>
    <p>With a global presence, we deliver reliable legal support services both remotely and in-office, tailored to the needs of modern legal practices.</p>
  </div>
  <a class="abs btn about-btn">Learn More <span class="arrow"><svg width="18" height="14" viewBox="0 0 18 14"><path d="M1 7h15M10 1l6 6-6 6" fill="none" stroke="#111" stroke-width="2"/></svg></span></a>
  <div class="abs mission">
    <h3>Our Mission</h3>
    <p>To empower legal professionals with structured systems, skilled support, and actionable legal intelligence—so they can practice law with confidence, precision, and efficiency.</p>
  </div>
  <svg class="abs badge" width="126" height="126" viewBox="0 0 126 126" aria-label="20+ years of experience">
    <defs><path id="ring" d="M63,63 m-46,0 a46,46 0 1,1 92,0 a46,46 0 1,1 -92,0"/></defs>
    <circle cx="63" cy="63" r="62" fill="#e8ad08"/>
    <text font-family="Montserrat,sans-serif" font-size="12" fill="#111"><textPath href="#ring">Years of Experience · Years of Experience ·</textPath></text>
    <text x="63" y="72" text-anchor="middle" font-family="Montserrat,sans-serif" font-size="30" font-weight="700" fill="#111">20+</text>
  </svg>
</section>

<section>
  <div class="abs services"></div>
  <h2 class="abs services-title">Our Services</h2>
  <div class="abs svc-arrows">
    <span><svg width="10" height="12" viewBox="0 0 10 12"><path d="M7 1L2 6l5 5" fill="none" stroke="#111" stroke-width="2"/></svg></span>
    <span><svg width="10" height="12" viewBox="0 0 10 12"><path d="M3 1l5 5-5 5" fill="none" stroke="#111" stroke-width="2"/></svg></span>
  </div>
  <article class="abs card" style="left:137px">
    <div class="ph" role="img" aria-label="Photo of two colleagues working with a tablet" style="background:linear-gradient(135deg,#c9ced6,#7e8ea3)"></div>
    <h4>Law Office Management Systems</h4>
    <p>Specialized Implementation &amp; Training</p>
  </article>
  <article class="abs card" style="left:403px">
    <div class="ph" role="img" aria-label="Photo of a remote paralegal on a video call" style="background:linear-gradient(135deg,#8a9a6a,#4e4437)"></div>
    <h4>Paralegal<br>Services</h4>
    <p>Remote or In-Office Support</p>
  </article>
  <article class="abs card featured" style="left:667px">
    <div class="ph" role="img" aria-label="Image of a researcher with digital legal interface graphics" style="background:linear-gradient(135deg,#3b6f86,#16384a)"></div>
    <h4>Legal Research &amp; Intelligence</h4>
    <p>We provide in-depth legal research designed to support litigation strategy and informed case assessment.</p>
  </article>
  <article class="abs card" style="left:931px">
    <div class="ph" role="img" aria-label="Photo of a businessman holding a tablet" style="background:linear-gradient(135deg,#dfe6ec,#8b98a6)"></div>
    <h4>Service by<br>Mail</h4>
    <p>Ex- Parte Notice</p>
  </article>
</section>

<section>
  <div class="abs global" role="img" aria-label="Soft background of legal scales and network graphics"></div>
  <h2 class="abs h2 global-title">Global Presence</h2>
  <p class="abs global-text">Lantern Quillhouse operates with a global footprint, allowing us to support legal professionals across jurisdictions. Our secure remote capabilities ensure consistent, timely, and confidential service—wherever you practice.</p>
</section>

<section>
  <div class="abs why-photo" role="img" aria-label="Photo of two colleagues reviewing a document together"></div>
  <div class="abs why-panel"></div>
  <h2 class="abs h2 why-title">Why Lantern Quillhouse</h2>
  <ul class="abs why-list">
    <li>Expertise in legal operations and management systems</li>
    <li>Research-driven insights tailored to your case strategy</li>
    <li>Flexible service models: remote or in-office</li>
    <li>Process-focused solutions that create long-term value</li>
    <li>Confidential, detail-oriented, and compliance-focused support</li>
  </ul>
  <a class="abs btn why-btn">Learn More <span class="arrow"><svg width="18" height="14" viewBox="0 0 18 14"><path d="M1 7h15M10 1l6 6-6 6" fill="none" stroke="#111" stroke-width="2"/></svg></span></a>
</section>

<section>
  <div class="abs cta" role="img" aria-label="Dark background photo of an empty office"></div>
  <h2 class="abs cta-title">Get Expert Legal Management Support</h2>
  <p class="abs cta-text">Whether you are implementing a new law office management system, expanding paralegal capacity, conducting complex legal research, or navigating probate matters, Lantern Quillhouse is your trusted legal management partner.</p>
  <p class="abs cta-strong">Contact us today to learn how we can support your legal practice with precision and prudence.</p>
  <a class="abs btn cta-btn">Contact Us <span class="arrow"><svg width="18" height="14" viewBox="0 0 18 14"><path d="M1 7h15M10 1l6 6-6 6" fill="none" stroke="#111" stroke-width="2"/></svg></span></a>
</section>

<section>
  <div class="abs subscribe"></div>
  <h2 class="abs h2 sub-title">Stay informed. Stay secure.</h2>
  <p class="abs sub-label">Subscribe Here</p>
  <div class="abs field"><span>You@example.com</span><span class="submit">Submit</span></div>
  <p class="abs sub-note">Security evolves fast — stay informed. Subscribe for launch updates.</p>
</section>

<footer>
  <div class="abs foot-brand">LANTERN QUILLHOUSE</div>
  <nav class="abs foot-nav"><a>HOME</a><a>ABOUT US</a><a>SERVICES</a><a>WHY CHOOSE US</a><a>TESTIMONIALS</a><a>CONTACT US</a></nav>
  <div class="abs social"><span aria-label="Social link"></span><span aria-label="Social link"></span><span aria-label="Social link"></span></div>
  <div class="abs bottombar">
    <span class="l">Your Privacy Choices| Privacy | Policy | Terms</span>
    <span class="r">© 2025 | www.lanternquillhouse.com</span>
  </div>
</footer>

</body>
</html>
```